Bramwell Electrical Services Website

'Fennimore Electrical Services' is a leading electrician company based in Hertfordshire. We are a QUORVIN approved and registered company in the UK. We are also registered to carry out electrical installations under Building regulations compliance of the building regulations. As part of a wide range of electrical services, we have professional expertise in installation testing (landlords, periodic, insurance, emergency lighting & fire alarms) rewires, installations, electrical maintenance, security systems & portable appliance testing (PAT). We provide a bespoke service to suite the needs of High End clients so the site must reflect the type of clientele we are targeting

WE ARE A SMALL COMPANY AND ARE LOOKING FOR THE DESIGNERS TO ALSO IMPLEMENT THIS ONTO OUR DOMAIN NAME SO ITS A FULLY FUNCTIONAL FOR OUR CLIENTS WHEN WE FINISH THIS SIMPLE PROJECT

Target Market(s)

Estate Agents, High End Clients that require intallations in Multi Million pound houses

Industry/Entity Type

Electrician

Font styles to use
Serif
Sans Serif
Other font styles liked:
• Chose an elegant professional font

Requirements
Must have
• please look at www.fennimoreelectrical.co.uk (the current old site is down, and will go live in 24-48 hours so please get the content from there)

Luxury design, a wow factor when high end clients logon

the logo is Blue so a blue colour these for the branding is essential. We are open to your design ideas around the logo.

QUORVIN and Building regulations compliance and Circuit Assurance Guild are safety regulations so please add the logos a place on the site together.
Nice to have
• your creative input
Should not have
• to many conflicting colours, too many horrible bright colours

```html
<!DOCTYPE html>
<html lang="en">
<head>
<meta charset="utf-8">
<title>Fennimore Electrical Services</title>
<link rel="stylesheet" href="https://fonts.googleapis.com/css2?family=Lato:wght@400;700;900&display=swap">
<style>
:root{
  --brand:#1d4fd6;
  --brand-dark:#0f2a8c;
  --navy:#0c1c55;
  --footer-blue:#1d3e9e;
  --ink:#222;
  --muted:#555;
  --light:#f4f4f4;
  --white:#fff;
  --hero-deep:#0a1626;
  --hero-mid:#1e3f66;
}
*{box-sizing:border-box;margin:0;padding:0}
html,body{width:858px;height:1200px;overflow:hidden}
body{position:relative;background:var(--white);font-family:'Lato',Arial,sans-serif;color:var(--ink)}
.site-header{position:absolute;left:0;top:0;width:858px;height:80px;background:var(--white)}
.brand{position:absolute;left:136px;top:14px;display:flex;align-items:center;gap:8px}
.brand-mark{width:44px;height:44px;border-radius:50%;background:var(--brand-dark)}
.brand-name{font-weight:900;font-size:17px;color:var(--brand-dark);line-height:1}
.brand-tagline{font-weight:700;font-size:9.5px;color:var(--brand-dark);margin-top:3px;letter-spacing:.2px}
.main-nav{position:absolute;top:61px;left:362px;display:flex;align-items:center;font-size:11.5px;font-weight:700}
.main-nav a{color:var(--ink);text-decoration:none}
.main-nav a.active{color:var(--brand)}
.main-nav .sep{width:4px;height:4px;border-radius:50%;background:#444;margin:0 19px}
.dropdown{position:absolute;left:510px;top:80px;width:112px;background:var(--white);box-shadow:0 2px 4px rgba(0,0,0,.25);font-size:9px;font-weight:700}
.dropdown div{padding:5px 10px;color:#555;height:17px}
.dropdown .current{background:var(--brand);color:var(--white);height:22px;padding-top:6px}
.hero{position:absolute;left:0;top:80px;width:858px;height:363px;background:radial-gradient(ellipse at 70% 40%,var(--hero-mid),var(--hero-deep) 75%)}
.hero-photo{position:absolute;inset:0;background:linear-gradient(90deg,rgba(0,0,0,.55),rgba(0,0,0,0) 45%)}
.caption{position:absolute;left:400px;top:160px;width:330px;height:96px;background:rgba(10,20,40,.65);padding:9px 10px;color:var(--white)}
.caption h2{font-size:26px;font-weight:700;line-height:1.1}
.caption p{font-size:11px;line-height:1.2;margin-top:9px;letter-spacing:-.1px}
.caption a{display:block;font-size:11px;color:#3fb0ff;font-style:italic;text-decoration:underline}
.btn-more{position:absolute;left:600px;top:282px;width:106px;height:28px;background:var(--brand);color:var(--white);font-weight:900;font-size:14px;text-align:center;line-height:28px;border-radius:2px}
.arrow{position:absolute;top:170px}
.dots{position:absolute;left:406px;top:344px;display:flex;gap:8px}
.dots span{width:8px;height:8px;border-radius:50%;background:#888}
.dots span.on{background:var(--brand)}
.welcome{position:absolute;left:0;top:443px;width:858px;height:144px;background:var(--light);text-align:center}
.section-title{font-size:17px;font-weight:700;color:#333}
.section-title em{font-style:normal;color:var(--brand)}
.welcome .section-title{margin-top:26px}
.welcome p{width:590px;margin:7px auto 0;font-size:11.3px;line-height:1.2;color:var(--muted)}
.features{position:absolute;left:137px;top:615px;display:flex;gap:17px}
.feature{width:183px;text-align:center;position:relative;height:222px}
.feature-photo{height:122px;background:linear-gradient(135deg,#8c9aa6,#c9b85a 55%,#4a5866)}
.feature h3{font-size:15px;font-weight:700;margin-top:4px;color:#333}
.feature h3 em{font-style:normal;color:var(--brand)}
.feature p{font-size:7.2px;line-height:1.4;color:var(--muted);margin-top:2px;text-align:justify;text-align-last:center}
.read-more{position:absolute;right:0;bottom:0;background:var(--brand);color:var(--white);font-size:7px;font-weight:900;padding:5px 4px;border-radius:2px}
.certs{position:absolute;left:0;top:896px;width:858px;height:106px;background:var(--light)}
.certs .section-title{position:absolute;left:0;width:858px;top:10px;text-align:center;color:#444;font-weight:900}
.cert{position:absolute;display:flex;align-items:center;justify-content:center}
.contact{position:absolute;left:0;top:1002px;width:858px;height:156px;background:var(--navy);color:var(--white);text-align:center}
.contact h2{font-size:17px;font-weight:700;margin-top:30px}
.contact .lead{font-size:11.5px;margin-top:9px;color:#dfe4f2}
.contact .details{font-size:7.5px;margin-top:12px;display:flex;justify-content:center;gap:14px;align-items:center}
.socials{display:flex;justify-content:center;gap:6px;margin-top:14px}
.socials span{width:15px;height:15px;border-radius:50%}
.site-footer{position:absolute;left:0;top:1158px;width:858px;height:42px;background:var(--footer-blue);color:var(--white);font-size:7.5px;text-align:center;line-height:42px}
</style>
</head>
<body>
<header class="site-header">
  <div class="brand">
    <span class="brand-mark"></span>
    <div>
      <div class="brand-name">FENNIMORE ELECTRICAL SERVICES</div>
      <div class="brand-tagline">QUALITY INSTALLATIONS &amp; HIGH STANDARDS</div>
    </div>
  </div>
  <nav class="main-nav">
    <a class="active" href="#">HOME</a><span class="sep"></span>
    <a href="#">ABOUT US</a><span class="sep"></span>
    <a href="#">SERVICES</a><span class="sep"></span>
    <a href="#">QUALITY</a><span class="sep"></span>
    <a href="#">CONTACT</a>
  </nav>
</header>

<section class="hero">
  <div class="hero-photo" role="img" aria-label="Electrician in a white hard hat inside an industrial plant, blue-toned"></div>
  <svg class="arrow" style="left:14px" width="18" height="26" viewBox="0 0 18 26"><path d="M14 2 4 13l10 11" fill="none" stroke="#bbb" stroke-width="4"/></svg>
  <svg class="arrow" style="left:826px" width="18" height="26" viewBox="0 0 18 26"><path d="M4 2l10 11L4 24" fill="none" stroke="#bbb" stroke-width="4"/></svg>
  <div class="caption">
    <h2>Superior Quality!</h2>
    <p>We promise our customers to continue to provide superior quality; whether in products, services, or workmanship.</p>
    <a href="#">Find out more about our commitment to our customers.</a>
  </div>
  <div class="btn-more">SEE MORE</div>
  <div class="dots"><span class="on"></span><span></span><span></span></div>
</section>
<div class="dropdown"><div>SERVICE 1</div><div class="current">SERVICE 2</div></div>

<section class="welcome">
  <h1 class="section-title">Welcome to <em>FENNIMORE</em></h1>
  <p>Fennimore Electrical Services Ltd is a well-established business whose workers have combined industry experience of over 30 years providing a first class reliable service in all fields of electrical contracting. We are pleased to offer advice over the telephone on various aspects of electrical installations relating to regulations. We offer free quotations and always welcome new business relationships with new clients and we endeavour to give new clients the same high standards that we give to our existing clients ....</p>
</section>

<section class="features">
  <article class="feature">
    <div class="feature-photo" role="img" aria-label="Electricians in hard hats inspecting a switchboard"></div>
    <h3>Committed to <em>Our Clients</em></h3>
    <p>Lorem ipsum dolor sit amet, consectetur adipiscing elit. Phasellus posuere neque ut massa scelerisque eu imperdiet purus pellentesque. Aenean nisl turpis, euismod vitae malesuada ac, sagittis sed. Lorem ipsum dolor sit amet, consectetur adipiscing elit. Phasellus posuere...</p>
    <span class="read-more">READ MORE</span>
  </article>
  <article class="feature">
    <div class="feature-photo" role="img" aria-label="Electrician in a hard hat working on a control panel"></div>
    <h3>The <em>Quality</em></h3>
    <p>We believe in the quality of all the work we conduct. We know that to succeed, you need reliable people, guaranteed products and a robust service you can count on. Fennimore Electrical Services have built a solid reputation with our high quality service divisions. To ensure that this ...</p>
    <span class="read-more">READ MORE</span>
  </article>
  <article class="feature">
    <div class="feature-photo" role="img" aria-label="Electricians in hard hats inspecting a switchboard"></div>
    <h3>Our <em>Services</em></h3>
    <p>The Electrical Service Divisions are the core of our business. We operate throughout the South East of England offering a 24hour call-out service for our clients. The electrical divisions offer complete installation services in all sectors, including domestic, commercial, retail ...</p>
    <span class="read-more">READ MORE</span>
  </article>
</section>

<section class="certs">
  <h2 class="section-title">OUR CERTIFICATIONS</h2>
  <div class="cert" style="left:186px;top:32px;width:74px;height:66px" role="img" aria-label="Circuit Assurance Guild certification badge">
    <svg width="60" height="60"><rect width="60" height="60" fill="#9b1c24"/></svg>
  </div>
  <div class="cert" style="left:330px;top:40px;width:200px;height:50px" role="img" aria-label="QUORVIN approved contractor badge">
    <svg width="180" height="40"><rect width="180" height="40" rx="4" fill="#1e78c8"/></svg>
  </div>
  <div class="cert" style="left:612px;top:30px;width:82px;height:70px" role="img" aria-label="Building regulations compliance certification badge">
    <svg width="62" height="62"><rect width="62" height="62" fill="#5aa832"/></svg>
  </div>
</section>

<section class="contact">
  <h2>Get in Touch</h2>
  <p class="lead">Vestibulum id ligula porta felis euismod semper,malesuada euismod.</p>
  <div class="details">
    <span><svg width="6" height="8" viewBox="0 0 6 8"><path d="M3 0a3 3 0 0 0-3 3c0 2 3 5 3 5s3-3 3-5a3 3 0 0 0-3-3z" fill="#fff"/></svg> Your Street No: 14/05 Light City, Country</span>
    <span><svg width="8" height="7" viewBox="0 0 8 7"><rect x="0" y="2" width="8" height="5" rx="1" fill="none" stroke="#fff"/><path d="M1 2V1h6v1" fill="none" stroke="#fff"/></svg> 0247 318 92 40</span>
  </div>
  <div class="socials">
    <span style="background:#e8a23c"></span>
    <span style="background:#3b66b0"></span>
    <span style="background:#4fa6dc"></span>
    <span style="background:#e2709e"></span>
    <span style="background:#c9393c"></span>
  </div>
</section>

<footer class="site-footer">© 2013 Copyright FENNIMORE ELECTRICAL SERVICES</footer>
</body>
</html>
```